Lube Haulz Poster- Graphic Design for Advertising Employment Opportunities.

LUBE HAULZ is a used motor oil collection and processing company.

We want to animate the truck and use it to create a graphic design used for advertising employment opportunities.

We need open areas to overlay custom wording.

This poster will be posted in truck stops, used at job fairs and advertised in newspapers.

Target Market(s)

Job seekers, skilled workers, truck drivers.

Industry/Entity Type

Recycling

Font styles to use
Serif
Sans Serif

Requirements
Must have
• Grayscale coloring preferred. Masculine. Complementing colors to the logo.
• Eye catching. Professional.
• MUST have open areas for customize-able wording.

```html
<!DOCTYPE html>
<html lang="en">
<head>
<meta charset="utf-8">
<title>Lube Haulz – We Are Hiring</title>
<link rel="stylesheet" href="https://fonts.googleapis.com/css2?family=Montserrat:wght@100;400;500;700;800&display=swap">
<style>
  :root {
    --navy: #070717;
    --slate: #6d6e71;
    --slate-light: #a3a4a7;
    --ink: #5f6062;
    --orange: #f15a29;
    --white: #ffffff;
    --muted: #8b8c90;
  }
  html, body { margin: 0; padding: 0; overflow: hidden; background: var(--white); }
  .canvas { position: relative; width: 849px; height: 1200px; overflow: hidden; }
  .poster {
    position: absolute; left: 0; top: 0;
    width: 1026px; height: 1450px;
    transform: scale(0.82749); transform-origin: 0 0;
    font-family: "Montserrat", Arial, sans-serif;
    background: var(--white);
  }
  .shapes { position: absolute; inset: 0; }
  .headline-small {
    position: absolute; right: 60px; top: 52px; margin: 0;
    font-size: 50px; font-weight: 700; color: var(--ink); line-height: 1;
  }
  .headline-big {
    position: absolute; right: 56px; top: 118px; margin: 0;
    font-size: 124px; font-weight: 100; color: var(--ink); line-height: 1;
    letter-spacing: 4px;
  }
  .band-title {
    position: absolute; left: 62px; top: 858px; width: 560px; margin: 0;
    transform: rotate(-14deg); transform-origin: 0 0;
    font-size: 38px; font-weight: 800; color: var(--white);
    text-align: center; line-height: 46px; white-space: nowrap;
    z-index: 2;
  }
  .band-title span { display: block; }
  .drop-text {
    position: absolute; left: 672px; top: 588px; width: 300px; margin: 0;
    text-align: center; color: var(--white);
    font-size: 31px; font-weight: 500; line-height: 39px;
  }
  .intro {
    position: absolute; left: 256px; top: 996px; width: 352px; margin: 0;
    font-size: 17.5px; line-height: 21px; color: var(--muted);
  }
  .divider { position: absolute; left: 256px; top: 1134px; width: 349px; height: 2px; background: var(--white); }
  .intro-note {
    position: absolute; left: 256px; top: 1153px; width: 352px; margin: 0;
    font-size: 17.5px; line-height: 21px; color: var(--white);
  }
  .perk {
    position: absolute; left: 627px; width: 399px; height: 98px;
    background: var(--slate); box-sizing: border-box; padding: 10px 18px 0 31px;
  }
  .perk h3 { margin: 0 0 6px; font-size: 23px; font-weight: 700; color: var(--orange); }
  .perk p { margin: 0; font-size: 17px; line-height: 21px; color: var(--white); }
  .brand {
    position: absolute; left: 66px; top: 1346px; margin: 0;
    font-size: 33px; font-weight: 700; color: var(--slate); line-height: 1;
  }
  .web {
    position: absolute; right: 33px; top: 1314px; margin: 0;
    font-size: 19px; font-weight: 500; color: var(--white); letter-spacing: 0.5px;
  }
  .footer-rule { position: absolute; left: 312px; top: 1347px; width: 714px; height: 4px; background: var(--orange); }
  .contact {
    position: absolute; right: 18px; top: 1357px; margin: 0;
    font-size: 17px; color: var(--muted); white-space: nowrap;
  }
  .contact .sep { color: var(--orange); margin: 0 12px; }
</style>
</head>
<body>
<div class="canvas">
  <div class="poster">
    <svg class="shapes" width="1026" height="1450" viewBox="0 0 1026 1450">
      <defs>
        <linearGradient id="sceneTone" x1="0" y1="0" x2="0" y2="1">
          <stop offset="0" stop-color="#2f6fc4"/>
          <stop offset="0.35" stop-color="#8fb5df"/>
          <stop offset="0.55" stop-color="#9a9a98"/>
          <stop offset="0.75" stop-color="#4a4a4c"/>
          <stop offset="1" stop-color="#8c8379"/>
        </linearGradient>
      </defs>
      <polygon class="lower-field" points="0,1005 1026,742 1026,1450 0,1450" fill="var(--navy)"/>
      <polygon class="truck-photo" role="img" aria-label="Photo of a chrome tanker truck parked on gravel beside storage tanks and a shed"
               points="0,118 1026,375 1026,742 0,1005" fill="url(#sceneTone)"/>
      <polygon class="corner-wedge" points="0,690 690,772 0,862" fill="var(--white)"/>
      <polygon class="title-band" points="0,862 740,682 740,812 0,1008" fill="var(--slate)"/>
      <polygon class="title-band-edge" points="0,988 740,798 740,812 0,1008" fill="var(--slate-light)"/>
      <path class="drop" d="M822 400 C870 500 977 600 977 720 A155 155 0 0 1 667 720 C667 600 774 500 822 400 Z" fill="var(--orange)"/>
    </svg>

    <h2 class="headline-small">We Are</h2>
    <h1 class="headline-big">HIRING!</h1>

    <p class="band-title"><span>SUB TITLE FOR CAMPAIGN</span><span>WILL BE HERE</span></p>

    <p class="drop-text">Grab<br>the opportunity<br>of a life time<br>and get ready<br>for a big<br>career leap!</p>

    <p class="intro">Lorem ipsum dolor sit amet,<br>consectetuer adipod tincidunt ut Lorem ipsum dolor sit amet, consectetuer amod tincidunt ut Lorem ipsum dolor sit amet, consectod tincidunt ut cidunt ut Lorem ipsum dolor sit amet</p>
    <div class="divider"></div>
    <p class="intro-note">Lorem ipsum dolor sit amet,<br>consectetuer adipod tincidunt ut Lorem ipsum dolor sit amet,</p>

    <div class="perk" style="top:910px">
      <h3>Bullet List 1</h3>
      <p>consectetuer adipod tincidunt ut Lorem ipsum dolor sit amet, consectetuer a</p>
    </div>
    <div class="perk" style="top:1037px">
      <h3>Bullet List 2</h3>
      <p>consectetuer adipod tincidunt ut Lorem ipsum dolor sit amet, consectetuer a</p>
    </div>
    <div class="perk" style="top:1165px">
      <h3>Bullet List 3</h3>
      <p>consectetuer adipod tincidunt ut Lorem ipsum dolor sit amet, consectetuer a</p>
    </div>

    <p class="brand">LUBE HAULZ</p>
    <p class="web">www.website.com</p>
    <div class="footer-rule"></div>
    <p class="contact">Ph : + 000 000 0000<span class="sep">|</span>Fax : + 000 000 0000<span class="sep">|</span>E-Mail : mail@mail.com</p>
  </div>
</div>
</body>
</html>
```